Business Card Design Project

We need a business card design for a consultancy called 'Amber Ridge'. The design should communicate innovation and professionalism. The colors used should complement our logo. Please include source files for winning design.
Updates

Industry/Entity Type

Business

Colors

Designer to choose colors to be used in the design.

Requirements
Must have
• Card size should be 85mm x 50mm. The back side of the card should be the logo on a black background. The front side should display the name 'Amber Ridge' along with standard information. The front's design should graphically complement the back.
Nice to have
• Any graphical elements in the front the complement the back side (with the logo on a black background) would be a plus.

```html
<!DOCTYPE html>
<html lang="en">
<head>
<meta charset="utf-8">
<title>Amber Ridge – Business Card</title>
<link rel="stylesheet" href="https://fonts.googleapis.com/css2?family=Crimson+Pro:wght@400&family=Arimo:wght@400&display=swap">
<style>
  :root {
    --page: #ffffff;
    --card: #000000;
    --label: #333333;
    --ink: #eeac6c;
    --wave-light: #fbe38e;
    --wave-mid: #f6b25a;
    --wave-deep: #ee6a1e;
    --emblem: #f39a30;
  }
  * { margin: 0; padding: 0; box-sizing: border-box; }
  html, body {
    width: 950px;
    height: 1200px;
    overflow: hidden;
    background: var(--page);
  }
  .sheet { position: relative; width: 950px; height: 1200px; }

  .side-label {
    position: absolute;
    left: 0;
    width: 950px;
    text-align: center;
    font-family: "Arimo", Arial, sans-serif;
    font-size: 78px;
    line-height: 1;
    color: var(--label);
  }
  .side-label--front { top: 2px; }
  .side-label--back { top: 603px; }

  .card {
    position: absolute;
    left: 0;
    width: 950px;
    background: var(--card);
    overflow: hidden;
    color: var(--ink);
    font-family: "Crimson Pro", Georgia, serif;
    font-weight: 400;
  }
  .card--front { top: 71px; height: 526px; }
  .card--back { top: 673px; height: 527px; }

  .company-name {
    position: absolute;
    left: 52px;
    top: 40px;
    font-size: 64px;
    line-height: 1;
    letter-spacing: 2px;
    text-transform: uppercase;
  }
  .waves { position: absolute; left: 0; top: 0; width: 950px; height: 526px; }

  .person-name {
    position: absolute;
    left: 106px;
    top: 150px;
    font-size: 76px;
    line-height: 1;
  }

  .contact {
    position: absolute;
    left: 108px;
    top: 280px;
    font-size: 44px;
    line-height: 54px;
  }
  .contact-row { display: flex; }
  .contact-label { width: 156px; }

  .emblem {
    position: absolute;
    left: 300px;
    top: 47px;
    width: 352px;
    height: 352px;
  }
  .brand-name {
    position: absolute;
    left: 0;
    width: 950px;
    top: 405px;
    text-align: center;
    font-size: 84px;
    line-height: 1;
    letter-spacing: 3px;
    text-transform: uppercase;
  }
</style>
</head>
<body>
<main class="sheet">
  <p class="side-label side-label--front">Front</p>

  <section class="card card--front" aria-label="Card front">
    <p class="company-name">Amber Ridge</p>

    <svg class="waves" viewBox="0 0 950 526" aria-hidden="true">
      <defs>
        <linearGradient id="wave-gradient" x1="0" y1="0" x2="1" y2="0">
          <stop offset="0" stop-color="var(--wave-light)"/>
          <stop offset="0.5" stop-color="var(--wave-mid)"/>
          <stop offset="1" stop-color="var(--wave-deep)"/>
        </linearGradient>
      </defs>
      <path d="M0 124 C 160 132, 330 128, 480 118 S 760 118, 950 122" fill="none" stroke="url(#wave-gradient)" stroke-width="8"/>
      <path d="M0 246 C 170 252, 340 246, 500 236 S 780 236, 950 241" fill="none" stroke="url(#wave-gradient)" stroke-width="8"/>
    </svg>

    <h1 class="person-name">Clara Wendt</h1>

    <div class="contact">
      <p class="contact-row"><span class="contact-label">Tel:</span><span>555 214 0387</span></p>
      <p class="contact-row"><span class="contact-label">E-mail:</span><span>clara.wendt@amberridge.com</span></p>
      <p class="contact-row"><span class="contact-label">Website:</span><span>www.amberridge.com</span></p>
    </div>
  </section>

  <p class="side-label side-label--back">Back</p>

  <section class="card card--back" aria-label="Card back">
    <svg class="emblem" viewBox="0 0 352 352" role="img" aria-label="Amber Ridge brand mark area">
      <circle cx="176" cy="176" r="176" fill="var(--emblem)"/>
    </svg>
    <p class="brand-name">Amber Ridge</p>
  </section>
</main>
</body>
</html>
```